Banner ads for VL that work with same theme as below banners

Love the banner ads below. Need more with attached photos. But use the same wording, font as in below banner ads. Should be VL size 1200/627 so I can use for Trovique and VL. Looking for great ads to use as VL ads. We do lots of ads so it will be worth your time to enter this contest you will be rewarded with a ton of work. Need several banner ads that work together. So maybe 1 of the dresses, 1 of the sweater, 1 of the leggings, 1 of the jacket

Target Market(s)

Women 24-45

Industry/Entity Type

Fashion

Requirements
Must have
• Banner ads that work for VL and Trovique
Nice to have
• Several options to choose from
Should not have
• not sure

```html
<!DOCTYPE html>
<html lang="en">
<head>
<meta charset="utf-8">
<title>Our Best Sweater Ever – Banner</title>
<link rel="stylesheet" href="https://fonts.googleapis.com/css2?family=Lobster&family=Roboto+Slab:wght@700&family=Raleway:wght@500&display=swap">
<style>
  :root {
    --wall-light: #f4efee;
    --wall-mid: #ece6e6;
    --wall-shade: #dcd8dc;
    --sweater-lilac: #b9b6cc;
    --sweater-shadow: #9d9bb3;
    --hair-tone: #8a6a44;
    --headline-white: #ffffff;
    --headline-dark: #3b3b3b;
    --headline-shadow: rgba(60, 55, 60, 0.55);
    --button-bg: #ffffff;
    --button-text: #2e2e2e;
    --button-text-soft: #555555;
  }
  * { margin: 0; padding: 0; box-sizing: border-box; }
  html, body { width: 1200px; height: 627px; overflow: hidden; }
  body { background: var(--wall-light); }

  .banner {
    position: relative;
    width: 1200px;
    height: 627px;
    overflow: hidden;
    background: linear-gradient(90deg, var(--wall-shade) 0%, var(--wall-mid) 40%, var(--wall-light) 70%, var(--wall-mid) 100%);
  }

  .banner__photo {
    position: absolute;
    left: 60px;
    top: 0;
    width: 380px;
    height: 627px;
    background:
      linear-gradient(180deg, var(--hair-tone) 0%, rgba(138,106,68,0.35) 22%, rgba(185,182,204,0) 36%),
      linear-gradient(90deg, var(--sweater-shadow) 0%, var(--sweater-lilac) 30%, var(--sweater-lilac) 75%, var(--sweater-shadow) 100%);
    opacity: 0.85;
  }

  .headline {
    position: absolute;
    left: 760px;
    top: 244px;
    width: 276px;
    text-align: center;
    font-family: "Lobster", cursive;
    line-height: 1.12;
  }
  .headline__line {
    display: block;
    font-size: 40px;
    color: var(--headline-white);
    text-shadow: 1px 2px 3px var(--headline-shadow);
    letter-spacing: 1px;
  }
  .headline__line--accent {
    color: var(--headline-dark);
    text-shadow: none;
    font-size: 41px;
  }

  .cta {
    position: absolute;
    left: 788px;
    top: 418px;
    width: 219px;
    height: 53px;
    background: var(--button-bg);
    display: flex;
    align-items: center;
    justify-content: center;
    gap: 7px;
    text-decoration: none;
    font-size: 15px;
    letter-spacing: 2px;
  }
  .cta__strong {
    font-family: "Roboto Slab", serif;
    font-weight: 700;
    color: var(--button-text);
  }
  .cta__soft {
    font-family: "Raleway", sans-serif;
    font-weight: 500;
    color: var(--button-text-soft);
  }
</style>
</head>
<body>
  <div class="banner">
    <div class="banner__photo" role="img" aria-label="Model with long wavy hair wearing an oversized lilac knit turtleneck sweater, leaning against a pale wall"></div>

    <h1 class="headline">
      <span class="headline__line">Our Best</span>
      <span class="headline__line headline__line--accent">Sweater</span>
      <span class="headline__line">Ever !</span>
    </h1>

    <a class="cta" href="#">
      <span class="cta__strong">SHOP</span>
      <span class="cta__soft">THE</span>
      <span class="cta__strong">LOOK</span>
    </a>
  </div>
</body>
</html>
```